Produktdisplays passend zur Produktverpackung
Ihr durchdachter und in sich stimmiger Designvorschlag hat uns überzeugt. Die Designerin hat unsere vielen Wünsche professionell und zeitnah umgesetzt und sie hat sich ideal in unsere Zielgruppe eingefühlt.
Zielgruppe
Wir sind ein Start-Up und haben einen Griffwärmer entwickelt. Unsere Zielgruppe sind vor allem Mütter mit Kinderwagen, aber auch Väter und Großeltern.
Aufgabenstellung
Die Verpackung existiert bereits, wir benötigen eure Unterstützung bei dem passenden Design dazu für einen Regal- sowie Thekendisplay. Verpackungsbilder der alten und neuen Verpackung, sowie Stanzkonturen und Bilderbeispiele der Displays sind angehängt.
Die Produktdisplays sollen die Aufmerksamkeit der Eltern im Winter auf sich ziehen und klar kommunizieren: Warme Hände, aktive Wärme für die Hände. Wie eine Griffheizung. Das Design sollte zu den Verpackungen passen, muss farblich aber nicht abgestimmt sein.
Sie sollten seriös wirken, also nicht offensichtlich vollständig von KI generiert. Das kann gut wirken, sollte dann aber durch Stockbilder etc verbessert werden.

```html
<!DOCTYPE html>
<html lang="de">
<head>
<meta charset="utf-8">
<title>Kaltfrei Werke – Regaldisplay</title>
<link rel="stylesheet" href="https://fonts.googleapis.com/css2?family=Inter:wght@500;600;700&display=swap">
<style>
  :root {
    --canvas-bg: #f4f1ee;
    --frame-tan: #b39880;
    --frame-edge: #f7e2c4;
    --panel-white: #ffffff;
    --ink: #1e1e1e;
    --ink-soft: #3a3a3a;
    --brand-orange: #e4572e;
    --brand-orange-light: #f27a4c;
    --brand-orange-dark: #c43f1c;
    --pack-text: #fff6f0;
    --sky-pale: #e9edf0;
    --sky-warm: #e6d9c8;
    --coat-beige: #b99a7c;
    --coat-pink: #d9c3c4;
    --coat-navy: #2b3344;
    --skin: #d9b49a;
    --stroller-dark: #2a2a2e;
    --grass: #8aa06a;
  }
  html, body {
    margin: 0;
    padding: 0;
    width: 1200px;
    height: 1200px;
    overflow: hidden;
    background: var(--canvas-bg);
    font-family: "Inter", Arial, sans-serif;
  }
  .display {
    position: absolute;
    left: 60px;
    top: 60px;
    width: 1080px;
    height: 1080px;
    background: var(--frame-tan);
    border-radius: 150px 150px 0 0;
    box-shadow: inset 0 0 0 8px var(--frame-edge), inset 0 0 40px rgba(247, 226, 196, 0.6);
  }
  .photo-column {
    position: absolute;
    top: 100px;
    width: 260px;
  }
  .photo-column--left { left: 45px; }
  .photo-column--right { right: 45px; }
  .photo-tile {
    width: 260px;
    height: 196px;
    margin-bottom: 20px;
    border-radius: 10px;
    box-shadow: 0 0 0 3px rgba(247, 226, 196, 0.55);
  }
  .photo-tile--arched { border-radius: 110px 110px 10px 10px; }

  .photo-tile--portrait-beige {
    background: linear-gradient(180deg, var(--sky-pale) 0%, #d8d2c8 30%, var(--skin) 48%, var(--coat-beige) 72%, #4a3f36 100%);
  }
  .photo-tile--stroller-beige {
    background: linear-gradient(180deg, #c9ab8e 0%, var(--coat-beige) 35%, #d46a3e 55%, #6b5a4c 72%, var(--stroller-dark) 100%);
  }
  .photo-tile--portrait-sun {
    background: linear-gradient(180deg, #9fb8d4 0%, var(--sky-warm) 30%, var(--skin) 50%, #c2a184 75%, #8a6a4c 100%);
  }
  .photo-tile--stroller-sun {
    background: linear-gradient(180deg, #c7ab90 0%, #b89a7e 35%, #d4653a 55%, #5f5248 75%, var(--stroller-dark) 100%);
  }
  .photo-tile--portrait-pink {
    background: linear-gradient(180deg, #c9d3d8 0%, #6a5448 28%, var(--skin) 45%, var(--coat-pink) 75%, var(--grass) 100%);
  }
  .photo-tile--stroller-pink {
    background: linear-gradient(180deg, var(--coat-pink) 0%, #e0cccc 35%, #d9643a 55%, #7f8f62 75%, var(--stroller-dark) 100%);
  }
  .photo-tile--portrait-navy {
    background: linear-gradient(180deg, #f2f3f4 0%, #5a4236 25%, var(--skin) 45%, #3a4356 70%, var(--coat-navy) 100%);
  }
  .photo-tile--stroller-navy {
    background: linear-gradient(180deg, #eef0f2 0%, var(--coat-navy) 30%, #d9643a 55%, #2a3040 72%, var(--stroller-dark) 100%);
  }

  .center-panel {
    position: absolute;
    left: 350px;
    top: 80px;
    width: 380px;
    height: 920px;
    background: var(--panel-white);
    border-radius: 190px 190px 0 0;
    text-align: center;
  }
  .brand-name {
    margin-top: 170px;
    display: inline-flex;
    align-items: center;
    gap: 10px;
    font-size: 27px;
    font-weight: 600;
    color: var(--ink-soft);
    letter-spacing: -0.2px;
  }
  .brand-dot {
    width: 16px;
    height: 16px;
    background: var(--brand-orange);
    border-radius: 50%;
  }
  .product-pack {
    position: relative;
    margin: 56px auto 0;
    width: 210px;
    height: 330px;
    border-radius: 18px;
    background: linear-gradient(165deg, var(--brand-orange-light), var(--brand-orange) 50%, var(--brand-orange-dark));
    box-shadow: 0 10px 22px rgba(196, 63, 28, 0.25);
    color: var(--pack-text);
  }
  .pack-title {
    position: absolute;
    top: 140px;
    left: 0;
    right: 0;
    font-size: 22px;
    font-weight: 700;
  }
  .pack-claim {
    position: absolute;
    top: 215px;
    left: 0;
    right: 0;
    font-size: 17px;
    font-weight: 600;
    line-height: 1.3;
  }
  .pack-note {
    position: absolute;
    top: 282px;
    left: 0;
    right: 0;
    font-size: 11px;
    font-weight: 500;
    opacity: 0.75;
  }
  .tagline {
    position: absolute;
    left: 0;
    right: 0;
    top: 640px;
    margin: 0;
    font-size: 32px;
    font-weight: 500;
    line-height: 1.25;
    color: var(--ink);
  }
</style>
</head>
<body>
  <div class="display">
    <div class="photo-column photo-column--left">
      <div class="photo-tile photo-tile--arched photo-tile--portrait-beige" role="img" aria-label="Foto: lächelnde Mutter in beiger Winterjacke vor einem Haus"></div>
      <div class="photo-tile photo-tile--stroller-beige" role="img" aria-label="Foto: Hände am Kinderwagengriff mit orangem Griffwärmer"></div>
      <div class="photo-tile photo-tile--portrait-sun" role="img" aria-label="Foto: lächelnde Mutter im Wintermantel im Abendlicht"></div>
      <div class="photo-tile photo-tile--stroller-sun" role="img" aria-label="Foto: Hände halten orangen Griffwärmer am Kinderwagen"></div>
    </div>

    <div class="center-panel">
      <div class="brand-name"><span class="brand-dot"></span>Kaltfrei Werke</div>
      <div class="product-pack" role="img" aria-label="Produktverpackung des orangen Griffwärmers">
        <div class="pack-title">hands,</div>
        <div class="pack-claim">Active warmth<br>for the hands</div>
        <div class="pack-note">Griff Wärmer</div>
      </div>
      <p class="tagline">Warm Hands,<br>Active warmth<br>for the hands</p>
    </div>

    <div class="photo-column photo-column--right">
      <div class="photo-tile photo-tile--arched photo-tile--portrait-pink" role="img" aria-label="Foto: lächelnde Mutter in rosa Jacke im Garten"></div>
      <div class="photo-tile photo-tile--stroller-pink" role="img" aria-label="Foto: Hände am Kinderwagengriff mit orangem Griffwärmer"></div>
      <div class="photo-tile photo-tile--portrait-navy" role="img" aria-label="Foto: lächelnde Mutter in dunkelblauer Jacke"></div>
      <div class="photo-tile photo-tile--stroller-navy" role="img" aria-label="Foto: Hände halten orangen Griffwärmer am Kinderwagengriff"></div>
    </div>
  </div>
</body>
</html>
```